The Drawer Sage needs a business card

The drawer sage is a lead generation service serving the Custom Closet industry.

Here is the basic card information:

The Drawer Sage
Gregory Tessman
Owner/CEO
Maple Hollow, NC
704-555-0183 Cell
Email: gtessman@TheDrawerSage.example

Additional information for the card:

"High quality, flat rate lead generation exclusively for the custom closet industry"

Bullet points for the back:

- Low fixed cost
- Easy to budget
- Guaranteed qualified Leeds
- Exclusivity per city

Logo attached, head shot attached. Photos of closet systems attached

```html
<!DOCTYPE html>
<html lang="en">
<head>
<meta charset="utf-8">
<title>The Drawer Sage — Business Card</title>
<link rel="stylesheet" href="https://fonts.googleapis.com/css2?family=Libre+Baskerville:wght@400;700&display=swap">
<style>
  :root {
    --copper: #a5672f;
    --slate: #545458;
    --paper: #ffffff;
    --ink: #4a4a4e;
    --backdrop: #2f2f31;
    --photo-light: #c9b7a6;
    --photo-dark: #2b3447;
  }
  * { box-sizing: border-box; margin: 0; padding: 0; }
  html, body {
    width: 1200px; height: 900px; overflow: hidden;
    background: var(--backdrop);
    font-family: "Libre Baskerville", Georgia, serif;
  }
  .canvas { position: relative; width: 1200px; height: 900px; }
  .card {
    position: absolute; width: 720px; height: 410px;
    border-radius: 22px; overflow: hidden;
    box-shadow: 0 14px 30px rgba(0,0,0,0.45);
  }

  /* Back side */
  .card-back { left: 80px; top: 30px; background: var(--slate); color: var(--paper); text-align: center; }
  .card-back .brand-name {
    position: absolute; left: 0; right: 0; top: 105px;
    font-size: 46px; font-weight: 400; color: var(--copper);
  }
  .card-back .brand-name::before {
    content: ""; display: inline-block; width: 14px; height: 14px;
    border-radius: 50%; background: var(--copper);
    margin-right: 16px; vertical-align: middle;
  }
  .tagline {
    position: absolute; left: 50px; right: 50px; top: 210px;
    font-size: 19px; font-weight: 700; line-height: 1.45;
  }
  .benefits {
    position: absolute; left: 20px; right: 20px; top: 315px;
    list-style: none; display: flex; justify-content: center; flex-wrap: wrap;
    font-size: 13.5px;
  }
  .benefits li + li::before {
    content: "•"; color: var(--copper); margin: 0 9px;
  }

  /* Front side */
  .card-front { left: 400px; top: 465px; background: var(--paper); }
  .card-front .brand-name {
    position: absolute; left: 50px; top: 88px;
    font-size: 34px; font-weight: 400; color: var(--copper);
  }
  .name-band {
    position: absolute; left: 0; right: 0; top: 176px; height: 70px;
    background: var(--copper); color: var(--paper);
    padding: 9px 0 0 50px;
  }
  .person-name { font-size: 30px; font-weight: 700; line-height: 1.1; }
  .person-title { font-size: 15px; margin-top: 3px; }
  .contact-list {
    position: absolute; left: 50px; top: 268px; list-style: none;
    font-size: 16px; color: var(--ink);
  }
  .contact-list li { display: flex; align-items: center; height: 29px; }
  .contact-list svg { width: 15px; height: 15px; margin-right: 12px; fill: var(--copper); flex: none; }
  .contact-list .accent { color: var(--copper); }
  .headshot-frame {
    position: absolute; right: 40px; top: 60px; width: 240px; height: 230px;
    border: 2px solid var(--copper); border-radius: 22px; background: var(--paper);
    padding: 10px; display: flex; justify-content: flex-end;
  }
  .headshot {
    width: 180px; height: 100%; border-radius: 14px;
    background: linear-gradient(160deg, var(--photo-light) 0%, #8f7a68 45%, var(--photo-dark) 100%);
  }
</style>
</head>
<body>
<main class="canvas">

  <section class="card card-back">
    <p class="brand-name">The Drawer Sage</p>
    <p class="tagline">High quality, flat rate lead generation exclusively for the custom closet industry</p>
    <ul class="benefits">
      <li>Low fixed cost</li>
      <li>Easy to budget</li>
      <li>Guaranteed qualified Leeds</li>
      <li>Exclusivity per city</li>
    </ul>
  </section>

  <section class="card card-front">
    <p class="brand-name">The Drawer Sage</p>
    <div class="name-band">
      <p class="person-name">Gregory Tessman</p>
      <p class="person-title">Owner/CEO</p>
    </div>
    <div class="headshot-frame">
      <div class="headshot" role="img" aria-label="Headshot of Gregory Tessman in a navy blazer"></div>
    </div>
    <ul class="contact-list">
      <li>
        <svg viewBox="0 0 24 24" aria-hidden="true"><path d="M6.6 10.8a15 15 0 0 0 6.6 6.6l2.2-2.2a1 1 0 0 1 1-.25 11.4 11.4 0 0 0 3.6.57 1 1 0 0 1 1 1V20a1 1 0 0 1-1 1A17 17 0 0 1 3 4a1 1 0 0 1 1-1h3.5a1 1 0 0 1 1 1c0 1.250.2 2.45.57 3.57a1 1 0 0 1-.25 1z"/></svg>
        704-555-0183
      </li>
      <li>
        <svg viewBox="0 0 24 24" aria-hidden="true"><path d="M3 5h18a1 1 0 0 1 1 1v12a1 1 0 0 1-1 1H3a1 1 0 0 1-1-1V6a1 1 0 0 1 1-1zm9 7.5L4 7.2V8l8 5.3L20 8v-.8z"/></svg>
        gtessman@TheDrawerSage.example
      </li>
      <li>
        <svg viewBox="0 0 24 24" aria-hidden="true"><path d="M12 2a10 10 0 1 0 0 20 10 10 0 0 0 0-20zm0 2c.9 0 2.2 2 2.7 5H9.3c.5-3 1.8-5 2.7-5zM4.3 11h3a17 17 0 0 0 0 2h-3a8 8 0 0 1 0-2zm5 0h5.4a15 15 0 0 1 0 2H9.3a15 15 0 0 1 0-2zm7.4 0h3a8 8 0 0 1 0 2h-3a17 17 0 0 0 0-2zM9.3 15h5.4c-.5 3-1.8 5-2.7 5s-2.2-2-2.7-5z"/></svg>
        www.<span class="accent">thedrawersage</span>.example
      </li>
      <li>
        <svg viewBox="0 0 24 24" aria-hidden="true"><path d="M12 2a7 7 0 0 0-7 7c0 5 7 13 7 13s7-8 7-13a7 7 0 0 0-7-7zm0 9.5A2.5 2.5 0 1 1 12 6.5a2.5 2.5 0 0 1 0 5z"/></svg>
        Maple Hollow, NC
      </li>
    </ul>
  </section>

</main>
</body>
</html>
```